Packaging Design for Fruit Juice Product

The Product is a fruit juice product. Kindly refer to the photograph attached for the temporary bottle shape and label position. (Please note that the cap colour will be different (not green), as it will be adjusted with the label design)

The fruit is Carica (it's similar like Papaya, but just in yellow color and smaller size). Like the other juice products, the target market covers most of the age range from 10 - 60 years old.

The temporary product name is: KEM

The fact that this juice product is quite unique, I want the product design to be something revolutionary and 'epic'.
The graphic design could be anything depends on your imagination. Basically, I want you to expand your creativity in designing the logo and the overall graphic design for the label.

- Do not design something ordinary or mediocre. Be Extraordinary -

*****The information below may / may not be used to base the label design. It is all up to you to decide whether it is useful in designing the label or not*****

I also have attached the basic information of the fruit and the place where the Carica tree grows: Dieng Plateau.
Dieng Plateau is Highland area where there are mountains. This Dieng Plateau is believed to be the place where the Gods live in the past.
This is probably because of the beautiful landscapes and the epic nature gift such as multi colour lakes, Volcanic crater, etc. (There are lots of myth about this place anyway).
Updates

There are lots of amazing and absolutely great designs on these websites:
You may want to check for the inspiration of our Fruit Juice Project 

Industry/Entity Type

Graphic Design

Requirements
Must have
• Remarkable logo and graphic design.

```html
<!DOCTYPE html>
<html lang="en">
<head>
<meta charset="utf-8">
<title>KEM Carica Juice – Label</title>
<link rel="stylesheet" href="https://fonts.googleapis.com/css2?family=Montserrat:wght@800;900&family=Roboto+Condensed:wght@700&display=swap">
<style>
  :root {
    --canvas: #ffffff;
    --juice-deep: #f4b01c;
    --juice-mid: #f8c238;
    --juice-light: #fde08a;
    --band: #000000;
    --title: #f9d24a;
    --brand: #ffffff;
    --accent: #f08a1c;
    --fruit-main: #f7d35a;
    --fruit-swirl: #2db36f;
  }
  html, body {
    margin: 0;
    padding: 0;
    width: 1200px;
    height: 1000px;
    overflow: hidden;
    background: var(--canvas);
  }
  .canvas {
    position: relative;
    width: 1200px;
    height: 1000px;
  }
  .label {
    position: absolute;
    left: 360px;
    top: 120px;
    width: 480px;
    height: 760px;
    background: linear-gradient(90deg, var(--juice-deep) 0%, var(--juice-mid) 45%, var(--juice-light) 80%, var(--juice-mid) 100%);
    overflow: hidden;
  }
  .brand-name {
    position: absolute;
    left: 50px;
    top: 6px;
    margin: 0;
    font-family: "Montserrat", sans-serif;
    font-weight: 900;
    font-size: 66px;
    line-height: 1;
    color: var(--brand);
    letter-spacing: -1px;
  }
  .title-band {
    position: absolute;
    left: 50px;
    top: 86px;
    width: 166px;
    height: 660px;
    background: var(--band);
  }
  .product-title {
    position: absolute;
    left: 50%;
    top: 50%;
    margin: 0;
    transform: translate(-50%, -50%) rotate(-90deg);
    white-space: nowrap;
    font-family: "Montserrat", sans-serif;
    font-weight: 900;
    font-size: 86px;
    line-height: 1;
    letter-spacing: 2px;
    color: var(--title);
  }
  .fruit-art {
    position: absolute;
    left: 170px;
    top: 6px;
    width: 300px;
    height: 600px;
  }
  .origin-note {
    position: absolute;
    left: 268px;
    top: 626px;
    width: 200px;
    margin: 0;
    text-align: center;
    font-family: "Roboto Condensed", sans-serif;
    font-weight: 700;
    font-size: 19px;
    line-height: 1.15;
    color: var(--accent);
  }
  .volume {
    position: absolute;
    left: 268px;
    top: 690px;
    width: 200px;
    margin: 0;
    text-align: center;
    font-family: "Roboto Condensed", sans-serif;
    font-weight: 700;
    font-size: 30px;
    color: var(--accent);
  }
</style>
</head>
<body>
<main class="canvas">
  <section class="label">
    <p class="brand-name">KEM</p>
    <div class="title-band">
      <h1 class="product-title">CARICA JUICE</h1>
    </div>
    <svg class="fruit-art" viewBox="0 0 300 600" role="img" aria-label="Illustration of a whole and a halved yellow carica fruit with seeds, framed by green spiral ornaments">
      <defs>
        <radialGradient id="fruitTone" cx="50%" cy="55%" r="60%">
          <stop offset="0%" stop-color="#fbe7a0"/>
          <stop offset="70%" stop-color="#f7d35a"/>
          <stop offset="100%" stop-color="#9fcf7e"/>
        </radialGradient>
      </defs>
      <rect x="10" y="10" width="280" height="580" rx="140" fill="url(#fruitTone)"/>
    </svg>
    <p class="origin-note">Indonesian Fruit<br>from Dieng Plateau</p>
    <p class="volume">750 ml</p>
  </section>
</main>
</body>
</html>
```